Verdant Banner Design

We need 3 Banners for our superfood supplement e-commerce store.

1. Banner that advertises the food combining chart Dimensions 417 × 464 https://verdantlift.net/content/11-food-combining-rules

2. We need a banner that advertises our subscription program. (Dimensions 388 × 219)

3. We need a banner that highlights our ingredients. (Dimensions 388 × 215)

Our website: https://verdantlift.net/

1. The sizes are in dimensions.

2. Yes the banners are for our website, replacing the ones on the front page now https://verdantlift.net/

Content of Banners

1. Advertisng the food combining chart.

2. Advertising our Subscription program.

3 Advertising our ingredients.

Just use words like:

"Combine the right foods"

Target Market(s)

Organic Superfood Supplement

Contact Information for Business Card

The Business card has to be double sided and must have our logo

Colors

Designer to choose colors to be used in the design.

Requirements
Must have
• 1. You can use the attached images or not, it is up to you, please be creative.
• 2. Please provide the Raw AI files, and also give it in the following formats: JPEG, PNG,
• 3. I have added a file in the brief called subscription image please use to get an idea of the type of banner we are looking for, of course using our product images
Nice to have
• 1. Please show business card design as well, this will help us decide to choose you.
• 2. Please read the ingredients on the product itself, and if you can use some images for the ingredient banner that would be good.
• 3. The business card should have the following:
• Name: Rupert Halvey
• Title: Co-Founder
• Address: Maplewick, NY
• Logo (see attached)
• Phone #: 855-640-3918
• Mobile #: 646-508-2274
• Email: info@verdantlift.net
• Website: www.verdantlift.net
Should not have
• No meat or dairy products in your images

```html
<!DOCTYPE html>
<html lang="en">
<head>
<meta charset="utf-8">
<title>Verdant Lift – Business Card</title>
<link href="https://fonts.googleapis.com/css2?family=Open+Sans:wght@400;600;700;800&display=swap" rel="stylesheet">
<style>
  :root {
    --backdrop: #e2e3e5;
    --card: #ffffff;
    --leaf: #86c705;
    --forest: #3b7d0c;
    --ink: #111111;
    --label: #2b2b2b;
    --divider: #b5b5b5;
    --panel: #fbfdfd;
  }
  * { margin: 0; padding: 0; box-sizing: border-box; }
  html, body {
    width: 1015px; height: 1200px; overflow: hidden;
    background: var(--backdrop);
    font-family: "Open Sans", Arial, sans-serif;
  }
  .sheet { position: relative; width: 1015px; height: 1200px; }
  .side-label {
    position: absolute; left: 97px;
    font-size: 13px; color: var(--label); letter-spacing: .2px;
  }
  .side-label--front { top: 55px; }
  .side-label--back { top: 606px; }
  .card {
    position: absolute; left: 98px; width: 820px;
    background: var(--card);
    box-shadow: 0 6px 22px rgba(0,0,0,.10);
    overflow: hidden;
  }
  .card--front { top: 82px; height: 470px; }
  .card--back { top: 637px; height: 472px; }
  .card__wave { position: absolute; inset: 0; width: 100%; height: 100%; }

  .brand {
    position: absolute; left: 0; right: 0; top: 92px; text-align: center;
  }
  .brand__name {
    display: block; color: var(--forest);
    font-weight: 800; font-size: 64px; line-height: 1; letter-spacing: -1px;
  }
  .brand__tagline {
    display: block; margin-top: 16px;
    font-size: 16px; color: var(--ink); font-weight: 400;
  }

  .holder__name {
    position: absolute; top: 366px; width: 100%; text-align: center; color: #fff;
    font-weight: 700; font-size: 17px; letter-spacing: .3px;
  }
  .holder__title {
    position: absolute; top: 395px; width: 100%; text-align: center; color: #fff;
    font-size: 14px; letter-spacing: .3px;
  }

  .badge {
    position: absolute; left: 334px; top: 1px; width: 166px; height: 154px;
    background: var(--panel); text-align: center;
  }
  .badge__square {
    display: block; width: 18px; height: 18px; margin: 28px auto 8px;
    background: var(--leaf);
  }
  .badge__name {
    display: block; color: var(--forest);
    font-weight: 800; font-size: 24px; line-height: 1.1;
  }
  .badge__place {
    position: absolute; left: 0; right: 0; top: 122px;
    font-weight: 800; font-size: 16px; color: var(--ink); letter-spacing: .3px;
  }

  .divider {
    position: absolute; left: 415px; top: 173px; width: 2px; height: 152px;
    background: var(--divider);
  }
  .contact { position: absolute; width: 200px; text-align: center; color: var(--ink); }
  .contact--phone { left: 202px; top: 206px; }
  .contact--mobile { left: 412px; top: 206px; }
  .contact__label { display: block; font-size: 9.5px; letter-spacing: .2px; }
  .contact__number { display: block; margin-top: 4px; font-size: 18px; }

  .link-row {
    position: absolute; top: 425px; display: flex; align-items: center;
    color: #fff; font-weight: 700; font-size: 16px;
  }
  .link-row--email { left: 28px; }
  .link-row--web { right: 25px; }
  .link-row svg { margin-right: 12px; }
</style>
</head>
<body>
<main class="sheet">
  <p class="side-label side-label--front">FRONT</p>
  <section class="card card--front">
    <svg class="card__wave" viewBox="0 0 820 470" preserveAspectRatio="none" aria-hidden="true">
      <polygon points="0,212 414,323 820,208 820,470 0,470" fill="var(--forest)"/>
      <polygon points="0,222 414,331 820,218 820,470 0,470" fill="var(--leaf)"/>
    </svg>
    <div class="brand">
      <span class="brand__name">Verdant Lift</span>
      <span class="brand__tagline">Verdant Foods For Today's Lifestyle</span>
    </div>
    <p class="holder__name">RUPERT HALVEY</p>
    <p class="holder__title">CO-FOUNDER</p>
  </section>

  <p class="side-label side-label--back">BACK</p>
  <section class="card card--back">
    <svg class="card__wave" viewBox="0 0 820 472" preserveAspectRatio="none" aria-hidden="true">
      <polygon points="0,213 416,325 820,210 820,472 0,472" fill="var(--forest)"/>
      <polygon points="0,223 416,331 820,220 820,472 0,472" fill="var(--leaf)"/>
    </svg>
    <div class="badge">
      <span class="badge__square"></span>
      <span class="badge__name">Verdant Lift</span>
      <p class="badge__place">MAPLEWICK, NY</p>
    </div>
    <div class="divider"></div>
    <div class="contact contact--phone">
      <span class="contact__label">PHONE #</span>
      <span class="contact__number">855-640-3918</span>
    </div>
    <div class="contact contact--mobile">
      <span class="contact__label">MOBILE #</span>
      <span class="contact__number">646-508-2274</span>
    </div>
    <div class="link-row link-row--email">
      <svg width="16" height="12" viewBox="0 0 16 12" aria-hidden="true">
        <rect x="0" y="0" width="16" height="12" rx="1.5" fill="#fff"/>
        <polyline points="1,1.5 8,7 15,1.5" fill="none" stroke="var(--leaf)" stroke-width="1.6"/>
      </svg>
      <span>info@verdantlift.net</span>
    </div>
    <div class="link-row link-row--web">
      <svg width="14" height="14" viewBox="0 0 14 14" aria-hidden="true">
        <circle cx="7" cy="7" r="6.5" fill="#fff"/>
        <ellipse cx="7" cy="7" rx="2.6" ry="6.2" fill="none" stroke="var(--leaf)" stroke-width="1.1"/>
        <line x1="0.8" y1="7" x2="13.2" y2="7" stroke="var(--leaf)" stroke-width="1.1"/>
      </svg>
      <span>www.verdantlift.net</span>
    </div>
  </section>
</main>
</body>
</html>
```